Cybersecurity company is looking for business card.

I need a business card design for our company, we are a cybersecurity company providing advance technology to protect agains any kind of malware. We need a fresh modern design it should communicate modern, technology and growth.

Target Market(s)

Business to business

Industry/Entity Type

Business

Contact Information for Business Card

Should have location, address, fax, mobile, phone, email and website.

Requirements
Must have
• Must follow company's logo color and style. Must have the company's log on its.

```html
<!DOCTYPE html>
<html lang="en">
<head>
<meta charset="utf-8">
<title>norvald business card</title>
<link rel="stylesheet" href="https://fonts.googleapis.com/css2?family=Open+Sans:wght@400;600;800&display=swap">
<style>
  :root {
    --page-bg: #5b3628;
    --card-dark: #000000;
    --card-light: #efefef;
    --brand-red: #a30f10;
    --mark-light: #e3e3e3;
    --ink: #111111;
  }
  * { margin: 0; padding: 0; box-sizing: border-box; }
  html, body { width: 1200px; height: 900px; overflow: hidden; }
  body {
    background: var(--page-bg);
    font-family: "Open Sans", Arial, sans-serif;
    position: relative;
  }
  .card {
    position: absolute;
    top: 319px;
    width: 443px;
    height: 260px;
    border-radius: 16px;
    overflow: hidden;
  }
  .card--back { left: 151px; background: var(--card-dark); }
  .card--front { left: 607px; background: var(--card-light); color: var(--ink); }

  .back-corner { position: absolute; left: 0; top: 0; }

  .wordmark {
    position: absolute;
    font-weight: 800;
    font-size: 46px;
    letter-spacing: 1px;
    line-height: 1;
    white-space: nowrap;
    transform: translate(-50%, -50%);
  }
  .card--back .wordmark { left: 221px; top: 133px; color: var(--mark-light); }
  .card--front .wordmark { left: 221px; top: 63px; color: var(--card-dark); }

  .accent-bar {
    position: absolute;
    top: 154px;
    width: 16px;
    height: 79px;
    background: var(--brand-red);
  }
  .accent-bar--left { left: 0; }
  .accent-bar--right { right: 0; }

  .holder {
    position: absolute;
    left: 28px;
    top: 168px;
    font-size: 8.5px;
    line-height: 12px;
  }
  .holder__name { font-size: 11.5px; line-height: 15px; margin-bottom: 1px; }

  .contact {
    position: absolute;
    right: 31px;
    top: 157px;
    text-align: right;
    font-size: 9.5px;
    line-height: 12.4px;
    font-family: Arial, "Open Sans", sans-serif;
  }
</style>
</head>
<body>
  <section class="card card--back" aria-label="Card back">
    <svg class="back-corner" width="170" height="170" viewBox="0 0 170 170" aria-hidden="true">
      <path d="M15 15 L159 15 L15 163 Z" fill="var(--brand-red)" stroke="var(--brand-red)" stroke-width="8" stroke-linejoin="round"/>
    </svg>
    <div class="wordmark">norvald</div>
  </section>

  <section class="card card--front" aria-label="Card front">
    <div class="wordmark">norvald</div>
    <span class="accent-bar accent-bar--left"></span>
    <span class="accent-bar accent-bar--right"></span>
    <div class="holder">
      <p class="holder__name">Idris Kalan</p>
      <p class="holder__title">Director of Information Technology</p>
      <p class="holder__mobile">M : +000 55 010 2040</p>
    </div>
    <address class="contact" style="font-style: normal;">
      Harbor Tech Park (HTP)<br>
      Meridian Avenue, Eastport - Nordland<br>
      T &nbsp;: +000 04 555 0188<br>
      F &nbsp;: +000 04 555 0189<br>
      E &nbsp;: idris.kalan@norvald.com<br>
      W : www.norvald.com
    </address>
  </section>
</body>
</html>
```